Need flyer for honey

I need the advertising flyer for my honey products. Will need around 4-6 page A5 size. Flyer content is ready but will need to check the wording and need the artwork and pictures designed in a proper manner.

Advertising

```html
<!DOCTYPE html>
<html lang="en">
<head>
<meta charset="UTF-8">
<title>Why Australian Honey? – Flyer</title>
<link rel="stylesheet" href="https://fonts.googleapis.com/css2?family=Lato:ital,wght@0,400;1,700;1,900&family=Oleo+Script:wght@700&display=swap">
<style>
  :root {
    --paper: #fffdf8;
    --paper-warm: #fbf1dc;
    --brown: #6b2f0c;
    --orange: #e0690f;
    --gold: #f2b21a;
    --text-grey: #6f6a66;
  }
  * { margin: 0; padding: 0; box-sizing: border-box; }
  html, body { width: 900px; height: 1200px; overflow: hidden; background: var(--paper); }
  .flyer {
    position: relative;
    width: 900px;
    height: 1200px;
    overflow: hidden;
    background: radial-gradient(ellipse at 70% 60%, var(--paper) 45%, var(--paper-warm) 100%);
    font-family: "Lato", sans-serif;
  }
  .flyer-art { position: absolute; inset: 0; width: 900px; height: 1200px; }

  .title {
    font-family: "Oleo Script", cursive;
    font-weight: 700;
    color: var(--brown);
  }
  .title-line {
    position: absolute;
    right: 40px;
    display: block;
    line-height: 1;
    white-space: nowrap;
  }
  .title-why { top: 318px; font-size: 62px; }
  .title-country { top: 392px; font-size: 50px; }
  .title-honey { top: 440px; font-size: 80px; color: var(--orange); }

  .benefit {
    position: absolute;
    right: 40px;
    text-align: right;
  }
  .benefit-heading {
    font-style: italic;
    font-weight: 900;
    font-size: 24px;
    line-height: 26px;
    color: var(--orange);
    margin-bottom: 4px;
  }
  .benefit-text {
    font-size: 15px;
    line-height: 19.6px;
    letter-spacing: 0.25px;
    color: var(--text-grey);
    white-space: nowrap;
  }
  .benefit-text + .benefit-text { margin-top: 10px; }

  .benefit-clean  { top: 558px; }
  .benefit-pure   { top: 712px; }
  .benefit-taste  { top: 888px; }
  .benefit-safety { top: 1014px; }
</style>
</head>
<body>
<main class="flyer">
  <svg class="flyer-art" viewBox="0 0 900 1200">
    <defs>
      <linearGradient id="heroTone" x1="0" y1="0" x2="1" y2="1">
        <stop offset="0" stop-color="#f6dc8a"/>
        <stop offset="0.35" stop-color="#e9a323"/>
        <stop offset="0.7" stop-color="#f4c03a"/>
        <stop offset="1" stop-color="#b8661a"/>
      </linearGradient>
      <radialGradient id="insetTone" cx="0.45" cy="0.55" r="0.6">
        <stop offset="0" stop-color="#f0a52a"/>
        <stop offset="0.6" stop-color="#f6c95a"/>
        <stop offset="1" stop-color="#fff2c4"/>
      </radialGradient>
      <linearGradient id="cornerTone" x1="0" y1="0" x2="1" y2="1">
        <stop offset="0" stop-color="#fbd86a"/>
        <stop offset="1" stop-color="#f0a820"/>
      </linearGradient>
    </defs>

    <path role="img" aria-label="Photo: glass jar of honey with wooden dipper, lemons and spices"
          transform="translate(0,-24)"
          d="M900,10 C820,200 700,330 540,395 C380,460 150,530 0,720 L0,0 H900 Z"
          fill="url(#heroTone)"/>

    <g fill="none">
      <path transform="translate(0,-12)" d="M900,10 C820,200 700,330 540,395 C380,460 150,530 0,720" stroke="#ffffff" stroke-width="22"/>
      <path d="M900,10 C820,200 700,330 540,395 C380,460 150,530 0,720" stroke="var(--brown)" stroke-width="18"/>
      <path transform="translate(0,20)" d="M900,10 C820,200 700,330 540,395 C380,460 150,530 0,720" stroke="var(--gold)" stroke-width="6" opacity="0.5"/>
    </g>

    <circle cx="458" cy="490" r="96" fill="var(--brown)"/>
    <circle cx="458" cy="490" r="90" fill="#ffffff"/>
    <circle role="img" aria-label="Photo: small jar of honey with a dipper" cx="458" cy="490" r="86" fill="url(#insetTone)"/>

    <path d="M0,1084 C140,1114 300,1160 420,1200 H0 Z" fill="var(--gold)"/>
    <path d="M0,1100 C140,1130 290,1170 380,1200 H0 Z" fill="#ffffff"/>
    <path d="M0,1114 C130,1142 270,1175 345,1200 H0 Z" fill="var(--brown)"/>
    <path role="img" aria-label="Photo: golden honeycomb" d="M0,1132 C120,1156 240,1182 300,1200 H0 Z" fill="url(#cornerTone)"/>
  </svg>

  <h1 class="title">
    <span class="title-line title-why">Why</span>
    <span class="title-line title-country">Australian</span>
    <span class="title-line title-honey">Honey?</span>
  </h1>

  <section class="benefit benefit-clean">
    <h2 class="benefit-heading">Clean &amp; Chemical Free</h2>
    <p class="benefit-text">Unlike many other countries producing honey, Australia has miles of pristine native forests<br>and diverse native flowers that are chemical free which provides the clean honey nectar<br>resources. Meanwhile, the honey bee industry is well protected by the National Biosecurity<br>Inspection Service which keeps industry free from varroa mite and other exotic diseases.<br>Very rare the chemicals are used in diseases control. Therefore from the very original source,<br>Australia honey is clean than from any other part of the world.</p>
  </section>

  <section class="benefit benefit-pure">
    <h2 class="benefit-heading">Pure &amp; Healthy</h2>
    <p class="benefit-text">Honey is healthy food, while many overseas honey producers are commercialized, who would minimize the<br>honey production circle to enhance production and adulterate their honey to make it a common<br>consistency. Color and flavor are controlled by adding additives, sugars, syrups and extenders</p>
    <p class="benefit-text">On the other hand, the Australian honey bee industry has a commitment to purity. Australian honey<br>producers do not use any of the additives or sugars to make their honey better looking. Instead, they insist to<br>make honey that is 100% pure and natural. Honey is left in the hives to let bee fan it until the water content<br>drops to a certain level while the nutrition level is protected and raised.</p>
  </section>

  <section class="benefit benefit-taste">
    <h2 class="benefit-heading">Unique Taste</h2>
    <p class="benefit-text">Australia is home to more than ten thousand species of plants and flowers, many of which are found nowhere<br>else in the world. The country’s unique native Eucalyptus trees and flowers create distinctive flavors of<br>honey. From dark amber to golden light in the color, Australia honey delivers various tastes from gentle<br>sweetness and mild caramel like to noticeable fragrance and sweet. Out of which everyone can find a taste of<br>his own.</p>
  </section>

  <section class="benefit benefit-safety">
    <h2 class="benefit-heading">Safety assured</h2>
    <p class="benefit-text">As a country prioritizes its people’s health and safety, the Australia government and regulation bodies have<br>established the world’s most strict food safety standards. There are also strict quality control procedures in<br>the honey &amp; bee industry that all apiarists and honey packers must adhere to. Therefore, Australia is the rare<br>country in the world that has very low risk of contamination from honey collection to packing and to<br>distribution.</p>
  </section>
</main>
</body>
</html>
```